BRIGHTDESK - Remote Tech Support Site

We are looking for a new very responsive and simple website for our brand Brightdesk.com - a remote technical support company.

This company supports customers Globally in different countries throughout Eur/ North America / South America / Asia etc (please keep this in mind and integrate into the idea).

Its important to us that the design is very explanatory, the customer should easily be able to figure out that we provide computer support right away ... I like one page responsive type designs as well without a bunch of menu items

Here are some similar sites we like - but still looking for a unique design that fits out brand "brightdesk" - I have upload also some layouts i like (but the designs are not important just the layouts), youll see it includes consumer business etc which is important.

VOLM.COM - I love how clean it is - nice and white easy to see everything

PLUMWIRE247.COM - also nice the layout and responsive one page design makes it easy to use

corvalfix.com - similar to plumwire design as well - you can get the idea im looking for between the two

You will notice those examples are much different then the attachments I added - again this is more of an idea for possible layouts .. attached is also the logo - could inspire color scheme / blue white black etc

Target Market(s)

Home consumers without computer knowledge , older age 45-65, small medium business ... computer repair - slow computers

Industry/Entity Type

Computer Repair

Logo Text

Brightdesk

Coding

Coded - Design and coding required

Number of Pages Required

1 page

Font styles to use
Sans Serif
Other font styles liked:
• your choice responsive

Colors

Designer to choose colors to be used in the design.

Requirements
Must have
• Clean - responsive - professional design - the name says it all - brightdesk
• CALL TO ACTIONS FOR "Get Help Now!" / "Learn More" etc
Nice to have
• We are looking for a new very responsive and simple website for our brand Brightdesk.com - a remote technical support company.
• This company supports customers Globally in different countries throughout Eur/ North America / South America / Asia etc (please keep this in mind and integrate into the idea).
• Its important to us that the design is very explanatory, the customer should easily be able to figure out that we provide computer support right away ... I like one page responsive type designs as well without a bunch of menu items
• Here are some similar sites we like - but still looking for a unique design that fits out brand "brightdesk" - I have upload also some layouts i like (but the designs are not important just the layouts), youll see it includes consumer business etc which is important.
• VOLM.COM - I love how clean it is - nice and white easy to see everything
• PLUMWIRE247.COM - also nice the layout and responsive one page design makes it easy to use
• corvalfix.com - similar to plumwire design as well - you can get the idea im looking for between the two
Should not have
• dark, packed page - bad small font -

```html
<!DOCTYPE html>
<html lang="en">
<head>
<meta charset="utf-8">
<title>Brightdesk – Remote Tech Support</title>
<link rel="stylesheet" href="https://fonts.googleapis.com/css2?family=Roboto:wght@300;400;500;700;900&family=Open+Sans:wght@400;600;700&display=swap">
<style>
:root{
  --blue:#1e88e5;
  --blue-dark:#1565c0;
  --navy:#0f2b4c;
  --green:#5bae3b;
  --green-dark:#47922b;
  --ink:#2b2b2b;
  --text:#5a5a5a;
  --muted:#8a8a8a;
  --line:#e2e2e2;
  --light:#f3f3f3;
  --footer:#2a2a2a;
  --footer-deep:#1f1f1f;
  --white:#ffffff;
}
*{box-sizing:border-box;margin:0;padding:0}
html,body{width:1200px;height:4986px;overflow:hidden}
body{font-family:"Open Sans",Arial,sans-serif;color:var(--text);background:var(--white);font-size:13px;line-height:1.55}
h1,h2,h3,h4{font-family:"Roboto",Arial,sans-serif;color:var(--ink)}
.section{position:relative;width:1200px;overflow:hidden}
.abs{position:absolute}
.btn{display:inline-flex;align-items:center;justify-content:center;font-family:"Roboto",Arial,sans-serif;font-weight:700;font-size:12px;text-transform:uppercase;letter-spacing:.5px;border-radius:3px;text-decoration:none}
.btn-blue{background:var(--blue);color:var(--white)}
.btn-green{background:var(--green);color:var(--white)}
.btn-outline{border:2px solid var(--ink);color:var(--ink);background:var(--white)}
.btn-white{background:var(--white);color:var(--ink)}
.photo{position:absolute}

/* top strip + nav */
.topbar{position:absolute;left:0;top:0;width:1200px;height:27px;background:var(--navy);color:#cfd8e3;font-size:11px;z-index:3}
.topbar .mail{position:absolute;left:160px;top:5px}
.topbar .region{position:absolute;right:160px;top:5px}
.navbar{position:absolute;left:0;top:27px;width:1200px;height:66px;background:rgba(20,60,110,.55);z-index:3}
.brand{position:absolute;left:160px;top:16px;display:flex;align-items:center;gap:10px;font-family:"Roboto",Arial,sans-serif;font-weight:700;font-size:28px;color:var(--white)}
.brand .dot{width:26px;height:26px;border-radius:50%;background:var(--blue)}
.menu{position:absolute;left:500px;top:24px;display:flex;gap:30px;font-family:"Roboto",Arial,sans-serif;font-size:12px;font-weight:500;color:var(--white)}
.phone-top{position:absolute;right:160px;top:18px;display:flex;align-items:center;gap:8px;font-family:"Roboto",Arial,sans-serif;font-weight:700;font-size:24px;color:var(--white)}

/* hero */
.hero{height:565px}
.hero .photo{left:0;top:0;width:1200px;height:565px;background:linear-gradient(100deg,#eef0f1 0%,#d9d6d0 40%,#c6bfb4 70%,#e6e2dc 100%)}
.hero-title{position:absolute;left:160px;top:172px;font-family:"Roboto",Arial,sans-serif;font-weight:700;font-size:42px;line-height:1.1;color:var(--blue)}
.hero .btn{position:absolute;left:160px;top:330px;width:166px;height:38px;text-transform:none;font-weight:500;font-size:13px}

/* member bar */
.member{position:absolute;left:160px;top:572px;width:877px;height:83px;background:var(--white);box-shadow:0 3px 14px rgba(0,0,0,.15);z-index:2}
.member .badge{position:absolute;left:0;top:0;width:160px;height:83px;background:var(--green);clip-path:polygon(0 0,100% 0,82% 100%,0 100%)}
.member .badge svg{position:absolute;left:42px;top:18px}
.member h3{position:absolute;left:200px;top:18px;font-size:22px;font-weight:700}
.member p{position:absolute;left:200px;top:48px;font-size:11px;color:var(--muted)}
.member .btn{position:absolute;right:20px;top:24px;width:120px;height:36px}

/* how it works */
.how{height:548px}
.sec-title{text-align:center;font-family:"Roboto",Arial,sans-serif;font-weight:700;font-size:28px;color:var(--ink)}
.how .sec-title{position:absolute;top:135px;width:100%}
.how .lead{position:absolute;left:160px;top:180px;width:880px;text-align:center;font-size:11px;color:var(--muted)}
.steps{position:absolute;left:160px;top:240px;width:880px;display:flex;justify-content:space-between}
.step{width:260px;text-align:center}
.step .icon{width:80px;height:80px;margin:0 auto 14px;border-radius:50%;border:2px solid var(--blue);display:flex;align-items:center;justify-content:center}
.step h4{font-size:16px;font-weight:500;margin-bottom:6px}
.step p{font-size:11px;color:var(--muted);line-height:1.5}
.how .btn{position:absolute;left:530px;top:485px;width:135px;height:38px}

/* about */
.about{height:466px;background:var(--white)}
.about .photo{left:0;top:0;width:615px;height:466px;background:linear-gradient(120deg,#e9ecef 0%,#cfd6dc 45%,#a9b2bb 80%,#8c96a0 100%)}
.about-text{position:absolute;left:650px;top:40px;width:500px}
.about-text h2{font-size:30px;font-weight:700;margin-bottom:14px}
.about-text p{font-size:12px;margin-bottom:14px;line-height:1.6}
.about .btn{position:absolute;left:650px;top:366px;width:130px;height:38px}
.about .mark{position:absolute;left:840px;top:368px;display:flex;align-items:center;gap:8px;font-family:"Roboto",Arial,sans-serif;font-weight:700;font-size:28px;color:var(--blue)}
.about .mark .dot{width:28px;height:28px;border-radius:50%;background:var(--blue)}

/* blue service band */
.services{height:183px;background:var(--blue);text-align:center;color:var(--white)}
.services h2{color:var(--white);font-size:30px;font-weight:500;padding-top:30px}
.services p{font-size:16px;color:#e3efff;margin-top:2px}
.services .btn{margin-top:16px;width:130px;height:38px;color:var(--blue)}

/* products */
.products{height:488px;background:linear-gradient(180deg,#6ab94a,#4e9e33)}
.products .sec-title{color:var(--white);padding-top:28px}
.product-row{position:absolute;left:160px;top:100px;width:880px;display:flex;justify-content:space-between}
.product{width:206px;text-align:center;color:var(--white)}
.product .shot{width:206px;height:236px;background:var(--white);padding:8px}
.product .shot div{width:100%;height:100%}
.product .name{font-size:11px;margin-top:8px;font-weight:600}
.product .price{font-family:"Roboto",Arial,sans-serif;font-size:26px;font-weight:700;margin-top:2px}
.product .actions{display:flex;justify-content:space-between;margin-top:10px}
.product .actions .btn{width:92px;height:28px;font-size:10px}

/* realtime */
.realtime{height:476px;background:#f1f1f1}
.realtime .photo{left:0;top:0;width:615px;height:476px;background:linear-gradient(110deg,#d8cbb8 0%,#bba488 50%,#8c7560 100%)}
.realtime-text{position:absolute;left:640px;top:70px;width:440px}
.realtime-text h2{font-size:44px;font-weight:900;line-height:1}
.realtime-text .sub{font-family:"Roboto",Arial,sans-serif;font-size:34px;font-weight:300;color:var(--ink);line-height:1.15;text-transform:uppercase}
.realtime-text .sub b{color:var(--blue);font-weight:700}
.checks{list-style:none;margin-top:22px}
.checks li{display:flex;align-items:center;gap:10px;font-size:12px;margin-bottom:8px}
.realtime .btn{position:absolute;left:640px;top:392px;width:165px;height:34px;font-size:11px}

/* features */
.features{height:492px;background:#e9ecef}
.features .photo{left:715px;top:0;width:485px;height:492px;background:linear-gradient(110deg,#e6e9ec 0%,#d5d6d3 40%,#b9b1a6 80%,#cfc9c1 100%)}
.features .panel-left{position:absolute;left:0;top:0;width:160px;height:492px;background:#dfe4e8}
.features .panel{position:absolute;left:160px;top:6px;width:555px;height:480px;background:var(--blue);color:var(--white);text-align:center}
.features h2{color:var(--white);font-size:34px;font-weight:700;margin-top:26px;line-height:1.1}
.features .at{font-family:"Roboto",Arial,sans-serif;font-size:17px;font-weight:500;color:var(--white);letter-spacing:.5px}
.feat-grid{display:grid;grid-template-columns:repeat(3,1fr);gap:26px 18px;padding:26px 38px 0}
.feat .ico{width:54px;height:54px;margin:0 auto 6px;border-radius:50%;border:2px solid var(--white);display:flex;align-items:center;justify-content:center}
.feat h4{color:var(--white);font-size:12px;font-weight:700;text-transform:uppercase}
.feat p{font-size:10px;color:#e3efff;line-height:1.4}
.features .btn{margin-top:22px;width:120px;height:32px;font-size:11px;background:var(--white);color:var(--blue)}

/* pricing */
.pricing{height:638px;background:var(--white)}
.pricing .sec-title{position:absolute;top:62px;width:100%;font-size:26px}
.pricing .sec-title span{color:var(--green)}
.plan{position:absolute;background:var(--white);text-align:center}
.plan-premium{left:160px;top:156px;width:289px;height:426px;border:1px solid var(--line)}
.plan-plus{left:449px;top:123px;width:309px;height:489px;box-shadow:0 4px 22px rgba(0,0,0,.2);z-index:2}
.plan-platinum{left:758px;top:156px;width:282px;height:426px;border:1px solid var(--line)}
.plan .head{height:56px;display:flex;align-items:center;justify-content:center;font-family:"Roboto",Arial,sans-serif;font-weight:700;font-size:16px;text-transform:uppercase;color:var(--white);background:var(--blue)}
.plan-plus .head{background:var(--green);height:66px;font-size:18px}
.plan .price{margin-top:22px;font-family:"Roboto",Arial,sans-serif;color:var(--ink)}
.plan .price b{font-size:38px;font-weight:700}
.plan .price sup{font-size:18px;vertical-align:top;position:relative;top:6px}
.plan .price small{font-size:12px;font-weight:700}
.plan .setup{font-size:11px;color:var(--muted)}
.plan .detail{margin-top:24px;background:var(--light);padding:16px 20px;font-size:12px;line-height:1.5}
.plan .detail b{color:var(--ink)}
.plan .btn{position:absolute;left:50%;transform:translateX(-50%);bottom:58px;width:170px;height:44px;border-radius:22px;justify-content:flex-start;padding-left:30px}
.plan-plus .btn{bottom:72px;width:210px;height:52px;border-radius:26px;padding-left:44px}
.plan .btn i{position:absolute;right:8px;width:28px;height:28px;border-radius:50%;background:var(--white);display:flex;align-items:center;justify-content:center}
.plan-plus .btn i{width:34px;height:34px}

/* testimonial */
.testimonial{height:216px}
.quote-box{position:absolute;left:160px;top:17px;width:880px;height:190px;border:1px solid var(--line);box-shadow:0 2px 10px rgba(0,0,0,.08)}
.quote-box .photo{left:0;top:0;width:190px;height:190px;background:linear-gradient(150deg,#cfd4d8,#8f979e)}
.quote-box .body{position:absolute;left:215px;top:18px;right:24px}
.quote-box .who{display:flex;align-items:center;gap:8px;font-family:"Roboto",Arial,sans-serif;font-size:17px;font-weight:500;color:var(--blue)}
.quote-box .who i{width:16px;height:16px;background:var(--blue);border-radius:2px}
.stars{display:flex;gap:3px;margin:4px 0 8px}
.quote-box p{font-size:11px;line-height:1.55}
.quote-box .more{color:var(--blue);font-size:11px;margin-top:4px}

/* client names */
.clients{height:142px}
.client-row{position:absolute;left:160px;top:20px;width:880px;height:86px;display:flex;border-top:1px solid var(--line);border-bottom:1px solid var(--line)}
.client{flex:1;display:flex;align-items:center;justify-content:center;font-family:"Roboto",Arial,sans-serif;font-weight:700;font-size:22px;color:#555;border-right:1px solid var(--line)}
.client:last-child{border-right:0}

/* consult cta */
.consult{height:356px;background:linear-gradient(180deg,#5fb340,#4c9d32)}
.consult .photo{left:160px;top:48px;width:420px;height:262px;border:6px solid var(--white);background:linear-gradient(130deg,#e6e2dc,#b8ad9f 60%,#8d8478)}
.consult-text{position:absolute;left:640px;top:60px;width:420px;color:var(--white)}
.consult-text h2{color:var(--white);font-size:28px;font-weight:700;line-height:1.15}
.consult-text .sub{font-family:"Roboto",Arial,sans-serif;font-size:23px;font-weight:300;line-height:1.2;margin-top:8px}
.consult-text .note{font-size:11px;margin-top:6px;color:#e8f5e0}
.consult .btn{position:absolute;left:758px;top:250px;width:164px;height:40px;gap:8px}

/* footer */
.footer{height:399px;background:var(--footer);color:#a8a8a8;font-size:11px}
.f-col{position:absolute;top:36px}
.f-brand{left:160px;width:280px}
.f-brand .logo{display:flex;align-items:center;gap:8px;font-family:"Roboto",Arial,sans-serif;font-weight:700;font-size:26px;color:var(--white);margin-bottom:16px}
.f-brand .logo .dot{width:26px;height:26px;border-radius:50%;background:var(--blue)}
.f-brand p{font-size:10px;line-height:1.5;margin-bottom:10px}
.f-col h4{color:var(--white);font-size:15px;font-weight:500;margin:6px 0 18px}
.f-col ul{list-style:none}
.f-col li{font-size:10px;margin-bottom:7px;display:flex;align-items:center;gap:6px}
.f-col li::before{content:"";width:4px;height:4px;border-radius:50%;background:#777}
.f-links{left:488px}
.f-support{left:693px}
.f-support li::before{display:none}
.f-plans{left:940px}
.socials{display:flex;gap:8px;margin-top:8px}
.socials span{width:20px;height:20px;border-radius:50%;background:#444}
.newsletter{position:absolute;left:160px;top:276px}
.newsletter h4{color:var(--white);font-size:14px;font-weight:500;margin-bottom:14px}
.newsletter form{display:flex}
.newsletter .field{width:300px;height:34px;background:#fff;color:#999;font-size:11px;padding:9px 12px}
.newsletter .btn{width:90px;height:34px;border-radius:0;text-transform:none;font-weight:500;font-size:13px}
.trusted{position:absolute;left:693px;top:260px}
.trusted h4{color:var(--white);font-size:14px;font-weight:500;margin-bottom:8px}
.seals{display:flex;gap:14px;align-items:center}
.seal-round{width:66px;height:66px;border-radius:50%;background:#c44}
.seal-round.gold{background:#c9a233}
.seal-rect{width:110px;height:40px;background:var(--white);border-radius:3px}
.copy{position:absolute;left:0;bottom:0;width:1200px;height:40px;background:var(--footer-deep)}
</style>
</head>
<body>

<div class="topbar">
  <span class="mail">info@brightdesk.com</span>
  <span class="region">United States ▾</span>
</div>
<nav class="navbar">
  <div class="brand"><span class="dot"></span>brightdesk</div>
  <div class="menu"><span>HOME</span><span>ABOUT US</span><span>SERVICES</span><span>CONTACT US</span></div>
  <div class="phone-top">
    <svg width="22" height="22" viewBox="0 0 24 24"><path fill="#fff" d="M6.6 10.8a15 15 0 0 0 6.6 6.6l2.2-2.2c.3-.3.7-.4 1-.2 1.1.4 2.3.6 3.6.6.6 0 1 .4 1 1V20c0 .6-.4 1-1 1A17 17 0 0 1 3 4c0-.6.4-1 1-1h3.5c.6 0 1 .4 1 1 0 1.3.2 2.5.6 3.6.1.3 0 .7-.2 1z"/></svg>
    (555) 010-2846
  </div>
</nav>

<header class="section hero">
  <div class="photo" role="img" aria-label="Smiling older couple relaxing at home with a laptop"></div>
  <h1 class="hero-title">Dedicated Support<br>Anytime.Anywhere</h1>
  <a class="btn btn-blue">Get FREE PC help now</a>
</header>

<div class="member">
  <div class="badge">
    <svg width="60" height="46" viewBox="0 0 60 46"><circle cx="30" cy="12" r="9" fill="#fff"/><path d="M14 44c0-10 7-17 16-17s16 7 16 17z" fill="#fff"/><circle cx="12" cy="16" r="6" fill="#fff" opacity=".8"/><circle cx="48" cy="16" r="6" fill="#fff" opacity=".8"/><path d="M0 40c0-8 5-13 12-13 3 0 5 1 7 2-4 3-6 7-6 11zM60 40c0-8-5-13-12-13-3 0-5 1-7 2 4 3 6 7 6 11z" fill="#fff" opacity=".8"/></svg>
  </div>
  <h3>BECOME A MEMBER TODAY!</h3>
  <p>Get priority help, yearly tune-ups and unlimited support for every device at home.</p>
  <a class="btn btn-green">GET IT NOW ›</a>
</div>

<section class="section how">
  <h2 class="sec-title">HOW IT WORKS</h2>
  <p class="lead">Getting help is easy. Call us or start a chat, let a certified technician connect to your computer securely, and watch your problem get solved in minutes, not days. We support homes and businesses in every time zone.</p>
  <div class="steps">
    <div class="step">
      <div class="icon"><svg width="40" height="36" viewBox="0 0 40 36"><rect x="2" y="2" width="36" height="24" rx="2" fill="none" stroke="#1e88e5" stroke-width="3"/><path d="M14 34h12M20 26v8" stroke="#1e88e5" stroke-width="3"/></svg></div>
      <h4>FREE Diagnostic</h4>
      <p>Tell us what is wrong and a technician checks your computer at no cost, then explains the fix in plain words before any work begins.</p>
    </div>
    <div class="step">
      <div class="icon"><svg width="36" height="36" viewBox="0 0 36 36"><path d="M24 4a8 8 0 0 0-7 11L4 28l4 4 13-13a8 8 0 0 0 11-7l-5 3-4-4z" fill="none" stroke="#1e88e5" stroke-width="3" stroke-linejoin="round"/></svg></div>
      <h4>Get Fixed</h4>
      <p>We remove viruses, speed up slow machines, fix email and printers and set up new software while you sit back and watch.</p>
    </div>
    <div class="step">
      <div class="icon"><svg width="36" height="36" viewBox="0 0 36 36"><path d="M18 4v20M10 16l8 8 8-8" fill="none" stroke="#1e88e5" stroke-width="3"/><path d="M4 26v6h28v-6" fill="none" stroke="#1e88e5" stroke-width="3"/></svg></div>
      <h4>Backup your information!</h4>
      <p>Keep photos, files and documents safe with automatic cloud backup, so nothing is lost if your computer ever fails again.</p>
    </div>
  </div>
  <a class="btn btn-outline">READ MORE ›</a>
</section>

<section class="section about">
  <div class="photo" role="img" aria-label="Technician in a suit helping a smiling client at a laptop"></div>
  <div class="about-text">
    <h2>ABOUT US</h2>
    <p>Brightdesk is a remote technical support company helping home users and small businesses across Europe, North America, South America and Asia. Our friendly technicians speak your language, work around the clock and never rush you. Whether your computer is slow, infected or simply confusing, we connect securely and fix it while you watch, with clear steps and no jargon along the way.</p>
    <p>We started with one simple idea: computer help should be easy for everyone. Today thousands of families and offices trust us with their devices, their data and their peace of mind. Every session is protected, every fix is guaranteed, and every customer gets a real person ready to answer questions at any hour.</p>
  </div>
  <a class="btn btn-outline">READ MORE ›</a>
  <div class="mark"><span class="dot"></span>brightdesk</div>
</section>

<section class="section services">
  <h2>Computer Repair and IT Support Services</h2>
  <p>We're a 24/7 Cost Efficient Tech Repair Services for You</p>
  <a class="btn btn-white">CONTACT US</a>
</section>

<section class="section products">
  <h2 class="sec-title">Our Products</h2>
  <div class="product-row">
    <div class="product">
      <div class="shot"><div role="img" aria-label="Laptop screen showing a protected status" style="background:linear-gradient(140deg,#8fd16a,#3f8d2a)"></div></div>
      <div class="name">Antivirus suite with live protection</div>
      <div class="price">$61.19</div>
      <div class="actions"><a class="btn btn-white">VIEW MORE</a><a class="btn btn-blue">ADD TO CART</a></div>
    </div>
    <div class="product">
      <div class="shot"><div role="img" aria-label="Computer screen with online security message" style="background:linear-gradient(140deg,#4a4f56,#1c2027)"></div></div>
      <div class="name">Online security for safe browsing</div>
      <div class="price">$61.19</div>
      <div class="actions"><a class="btn btn-white">VIEW MORE</a><a class="btn btn-blue">ADD TO CART</a></div>
    </div>
    <div class="product">
      <div class="shot"><div role="img" aria-label="Blue data privacy concept" style="background:linear-gradient(140deg,#8ec8ef,#2e78b8)"></div></div>
      <div class="name">Data privacy guard for every device</div>
      <div class="price">$61.19</div>
      <div class="actions"><a class="btn btn-white">VIEW MORE</a><a class="btn btn-blue">ADD TO CART</a></div>
    </div>
    <div class="product">
      <div class="shot"><div role="img" aria-label="Blue digital lock on a circuit board" style="background:linear-gradient(140deg,#a6d2f2,#3d7fb5)"></div></div>
      <div class="name">Secure lock for files and folders</div>
      <div class="price">$61.19</div>
      <div class="actions"><a class="btn btn-white">VIEW MORE</a><a class="btn btn-blue">ADD TO CART</a></div>
    </div>
  </div>
</section>

<section class="section realtime">
  <div class="photo" role="img" aria-label="Family smiling together at a home computer"></div>
  <div class="realtime-text">
    <h2>REAL-TIME</h2>
    <div class="sub">SUPPORT FEATURES AND <b>BENEFITS</b></div>
    <ul class="checks">
      <li><svg width="14" height="14" viewBox="0 0 14 14"><path d="M2 7l3 3 7-7" fill="none" stroke="#1e88e5" stroke-width="2"/></svg>24/7 Real Live Technician Support</li>
      <li><svg width="14" height="14" viewBox="0 0 14 14"><path d="M2 7l3 3 7-7" fill="none" stroke="#1e88e5" stroke-width="2"/></svg>The best security software in the market</li>
      <li><svg width="14" height="14" viewBox="0 0 14 14"><path d="M2 7l3 3 7-7" fill="none" stroke="#1e88e5" stroke-width="2"/></svg>Regular tune-ups and optimization</li>
      <li><svg width="14" height="14" viewBox="0 0 14 14"><path d="M2 7l3 3 7-7" fill="none" stroke="#1e88e5" stroke-width="2"/></svg>Setup and installation included</li>
    </ul>
  </div>
  <a class="btn btn-blue">BECOME A MEMBER ›</a>
</section>

<section class="section features">
  <div class="panel-left"></div>
  <div class="photo" role="img" aria-label="Young woman smiling while working on a laptop"></div>
  <div class="panel">
    <h2>ALL THE BEST FEATURES</h2>
    <div class="at">AT THE BEST PRICE!</div>
    <div class="feat-grid">
      <div class="feat"><div class="ico"><svg width="26" height="26" viewBox="0 0 26 26"><rect x="3" y="5" width="20" height="14" rx="1" fill="none" stroke="#fff" stroke-width="2"/><path d="M8 23h10" stroke="#fff" stroke-width="2"/></svg></div><h4>Ad Blocker</h4><p>Stop annoying pop-ups and keep pages clean while you browse.</p></div>
      <div class="feat"><div class="ico"><svg width="26" height="26" viewBox="0 0 26 26"><circle cx="13" cy="13" r="9" fill="none" stroke="#fff" stroke-width="2"/><path d="M13 8v5l4 3" stroke="#fff" stroke-width="2" fill="none"/></svg></div><h4>Regular Tune-ups</h4><p>Get a regular tune-up so your computer keeps running fast.</p></div>
      <div class="feat"><div class="ico"><svg width="26" height="26" viewBox="0 0 26 26"><path d="M4 22V12M10 22V6M16 22V14M22 22V9" stroke="#fff" stroke-width="2"/></svg></div><h4>System Reports</h4><p>Stay up to date with clear health reports for your PC.</p></div>
      <div class="feat"><div class="ico"><svg width="26" height="26" viewBox="0 0 26 26"><rect x="2" y="6" width="14" height="11" fill="none" stroke="#fff" stroke-width="2"/><rect x="18" y="9" width="6" height="11" fill="none" stroke="#fff" stroke-width="2"/></svg></div><h4>Multiple Devices</h4><p>Cover up to five computers, tablets and phones at home.</p></div>
      <div class="feat"><div class="ico"><svg width="26" height="26" viewBox="0 0 26 26"><rect x="8" y="3" width="10" height="20" rx="2" fill="none" stroke="#fff" stroke-width="2"/></svg></div><h4>Mobile Security</h4><p>Keep your phone safe from threats wherever you travel.</p></div>
      <div class="feat"><div class="ico"><svg width="26" height="26" viewBox="0 0 26 26"><path d="M7 19a5 5 0 0 1 0-10 7 7 0 0 1 13 2 4 4 0 0 1 0 8z" fill="none" stroke="#fff" stroke-width="2"/></svg></div><h4>Cloud Backup</h4><p>Never lose a file again with safe automatic online backup.</p></div>
    </div>
    <a class="btn">VIEW MORE ›</a>
  </div>
</section>

<section class="section pricing">
  <h2 class="sec-title">MEMBERSHIP PRICING AND <span>PLANS</span></h2>
  <div class="plan plan-premium">
    <div class="head">Premium</div>
    <div class="price"><sup>$</sup><b>19.99</b><small>/MONTHLY</small></div>
    <div class="setup">($249-$300 setup fee)</div>
    <div class="detail">Regular 90-Day Optimization<br><b>Unlimited 24/7 Tier 3 Technician Support</b></div>
    <a class="btn btn-blue">LEARN MORE<i><svg width="10" height="10" viewBox="0 0 10 10"><path d="M3 1l4 4-4 4" stroke="#1e88e5" stroke-width="2" fill="none"/></svg></i></a>
  </div>
  <div class="plan plan-plus">
    <div class="head">Premium Plus</div>
    <div class="price"><sup>$</sup><b>29.99</b><small>/MONTHLY</small></div>
    <div class="setup">($249-$300 setup fee)</div>
    <div class="detail">Regular 90-Day Optimization<br><b>Unlimited 24/7 Tier 3 Technician Support</b></div>
    <a class="btn btn-green">LEARN MORE<i><svg width="10" height="10" viewBox="0 0 10 10"><path d="M3 1l4 4-4 4" stroke="#5bae3b" stroke-width="2" fill="none"/></svg></i></a>
  </div>
  <div class="plan plan-platinum">
    <div class="head">Platinum</div>
    <div class="price"><sup>$</sup><b>19.99</b><small>/MONTHLY</small></div>
    <div class="setup">($249-$300 setup fee)</div>
    <div class="detail">Regular 90-Day Optimization<br><b>Unlimited 24/7 Tier 3 Technician Support</b></div>
    <a class="btn btn-blue">LEARN MORE<i><svg width="10" height="10" viewBox="0 0 10 10"><path d="M3 1l4 4-4 4" stroke="#1e88e5" stroke-width="2" fill="none"/></svg></i></a>
  </div>
</section>

<section class="section testimonial">
  <div class="quote-box">
    <div class="photo" role="img" aria-label="Portrait of a satisfied customer"></div>
    <div class="body">
      <div class="who"><i></i>Dana Whitfield</div>
      <div class="stars">
        <svg width="14" height="14" viewBox="0 0 14 14"><path d="M7 1l1.8 3.8 4.2.5-3.1 2.9.8 4.1L7 10.3 3.3 12.3l.8-4.1L1 5.3l4.2-.5z" fill="#1e88e5"/></svg>
        <svg width="14" height="14" viewBox="0 0 14 14"><path d="M7 1l1.8 3.8 4.2.5-3.1 2.9.8 4.1L7 10.3 3.3 12.3l.8-4.1L1 5.3l4.2-.5z" fill="#1e88e5"/></svg>
        <svg width="14" height="14" viewBox="0 0 14 14"><path d="M7 1l1.8 3.8 4.2.5-3.1 2.9.8 4.1L7 10.3 3.3 12.3l.8-4.1L1 5.3l4.2-.5z" fill="#1e88e5"/></svg>
        <svg width="14" height="14" viewBox="0 0 14 14"><path d="M7 1l1.8 3.8 4.2.5-3.1 2.9.8 4.1L7 10.3 3.3 12.3l.8-4.1L1 5.3l4.2-.5z" fill="#ccc"/></svg>
        <svg width="14" height="14" viewBox="0 0 14 14"><path d="M7 1l1.8 3.8 4.2.5-3.1 2.9.8 4.1L7 10.3 3.3 12.3l.8-4.1L1 5.3l4.2-.5z" fill="#ccc"/></svg>
      </div>
      <p>My laptop had become so slow I could barely open my email. I called in the evening and a technician connected within minutes, explained everything patiently and cleaned out years of clutter. It now starts up in seconds and runs like new. I have since signed up my husband's computer and the small office we run from home. Honest, kind and quick service, and no confusing words at all. I would recommend them to every friend who struggles with technology.</p>
      <div class="more">See More</div>
    </div>
  </div>
</section>

<section class="section clients">
  <div class="client-row">
    <div class="client">Northfield</div>
    <div class="client">KVR</div>
    <div class="client">Carelane</div>
    <div class="client">Medistra</div>
    <div class="client">Tallow</div>
  </div>
</section>

<section class="section consult">
  <div class="photo" role="img" aria-label="Older man smiling while using a laptop at home"></div>
  <div class="consult-text">
    <h2>GET A 30-MINUTE ONE-ON-ONE</h2>
    <div class="sub">FREE CONSULTATION WITH ONE<br>OF OUR EXPERTS! *</div>
    <div class="note">* Limited period offer</div>
  </div>
  <a class="btn btn-white">
    <svg width="14" height="14" viewBox="0 0 24 24"><path fill="#2b2b2b" d="M6.6 10.8a15 15 0 0 0 6.6 6.6l2.2-2.2c.3-.3.7-.4 1-.2 1.1.4 2.3.6 3.6.6.6 0 1 .4 1 1V20c0 .6-.4 1-1 1A17 17 0 0 1 3 4c0-.6.4-1 1-1h3.5c.6 0 1 .4 1 1 0 1.3.2 2.5.6 3.6.1.3 0 .7-.2 1z"/></svg>
    CALL US TODAY
  </a>
</section>

<footer class="section footer">
  <div class="f-col f-brand">
    <div class="logo"><span class="dot"></span>brightdesk</div>
    <p>We are a group of tech experts who work round the clock to keep your computers fast, safe and easy to use, for homes and businesses worldwide.</p>
    <p>Get in touch with our team any time of day, any day of the week. We offer friendly support in many languages.</p>
  </div>
  <div class="f-col f-links">
    <h4>Quick Links</h4>
    <ul><li>Home</li><li>About Us</li><li>Services</li><li>Contact Us</li><li>FAQs</li></ul>
  </div>
  <div class="f-col f-support">
    <h4>Our Support</h4>
    <ul><li>Help Center</li><li>info@brightdesk.com</li><li>(555) 010-2846</li></ul>
    <div class="socials"><span></span><span></span><span></span><span></span></div>
  </div>
  <div class="f-col f-plans">
    <h4>Plans</h4>
    <ul><li>Premium Plan</li><li>Premium Plus Plan</li><li>Platinum Plan</li></ul>
  </div>
  <div class="newsletter">
    <h4>Newsletter Signup</h4>
    <form><div class="field">Enter your email</div><a class="btn btn-blue">Sign up</a></form>
  </div>
  <div class="trusted">
    <h4>Trusted By</h4>
    <div class="seals">
      <div class="seal-round"></div>
      <div class="seal-round gold"></div>
      <div class="seal-rect"></div>
    </div>
  </div>
  <div class="copy"></div>
</footer>

</body>
</html>
```